Business Card Design Project- Removalist

I would like to surprise my husband to be with a different type of wedding present. His brother (who he owned a removalist business with) suddenly passed away from cancer recently and he has changed his business name to 'RTB' (which stands for Raising Tom Bright; but the full name doesn't need to be on the business card as it is more of a personal business name). To celebrate the new business I would like to get him some business cards made.
I would like the business name to be listed as 'RTB' and somewhere on the card I would like 'Sydney wide removals and relocation services'. I would like it to be obvious from the front of the card that it is a removalist business card. If a truck or some other feature that makes it look like a removalist business card could added it would be appreciated.
I don't mind what colours are used, but I would like the colour blue to feature somewhere in the design. It can be bright and fun, which is how Tom was.
I will also need the company's email address and phone number listed
The email address is: rtbremovals@quillpost.example
The contact number is: 0417 282 934
I don't need a contact name listed on the card, but perhaps 'Owned and operated by the Pendleworth family' could be added near the contact details in small font.
Thank you very much for considering this project!
Kind regards,
Fiona
Updates
Could you please change the mobile contact number to 0417 282 934. This is the only contact phone number required on the card now.
Thank you!

```html
<!DOCTYPE html>
<html lang="en">
<head>
<meta charset="utf-8">
<title>RTB Removals – Business Card</title>
<link rel="stylesheet" href="https://fonts.googleapis.com/css2?family=Open+Sans:wght@400&family=Dancing+Script:wght@500&display=swap">
<style>
  :root {
    --page: #f2f1ee;
    --kraft: #c8a67c;
    --kraft-edge: #b38f64;
    --brand-blue: #1ea7e8;
    --ink: #1d1a17;
  }
  * { box-sizing: border-box; margin: 0; padding: 0; }
  html, body {
    width: 828px;
    height: 1200px;
    overflow: hidden;
    background: var(--page);
  }
  .business-card {
    position: absolute;
    left: 94px;
    top: 417px;
    width: 640px;
    height: 366px;
    background: var(--kraft);
    border: 1px solid var(--kraft-edge);
  }
  .business-name {
    position: absolute;
    left: 44px;
    top: 40px;
    width: 300px;
    color: var(--brand-blue);
    font-family: "Open Sans", sans-serif;
    font-weight: 400;
    font-size: 64px;
    line-height: 1.1;
  }
  .family-line {
    position: absolute;
    left: 46px;
    top: 254px;
    color: var(--brand-blue);
    font-family: "Dancing Script", cursive;
    font-size: 17px;
  }
  .contact-block {
    position: absolute;
    left: 352px;
    top: 218px;
    display: flex;
    align-items: stretch;
    gap: 12px;
  }
  .contact-icons {
    display: flex;
    flex-direction: column;
    justify-content: flex-end;
    gap: 8px;
    padding-bottom: 2px;
  }
  .contact-icons svg { display: block; }
  .contact-rule {
    width: 1px;
    background: var(--ink);
  }
  .contact-details {
    font-family: "Open Sans", sans-serif;
    color: var(--ink);
    font-size: 14px;
    line-height: 1.45;
  }
  .service-area {
    text-transform: uppercase;
    letter-spacing: 0.3px;
    margin-bottom: 10px;
  }
</style>
</head>
<body>
  <section class="business-card" aria-label="RTB Removals business card">
    <h1 class="business-name">RTB<br>Removals</h1>
    <p class="family-line">Owned &amp; operated by the Pendleworth family</p>

    <div class="contact-block">
      <div class="contact-icons">
        <svg width="22" height="22" viewBox="0 0 22 22" aria-label="Email">
          <circle cx="11" cy="11" r="11" fill="var(--ink)"/>
          <rect x="5.5" y="7" width="11" height="8" fill="none" stroke="var(--kraft)" stroke-width="1.4"/>
          <path d="M5.5 7 L11 11.5 L16.5 7" fill="none" stroke="var(--kraft)" stroke-width="1.4"/>
        </svg>
        <svg width="22" height="22" viewBox="0 0 22 22" aria-label="Phone">
          <circle cx="11" cy="11" r="11" fill="var(--ink)"/>
          <rect x="7.5" y="4.5" width="7" height="13" rx="1.5" fill="none" stroke="var(--kraft)" stroke-width="1.4"/>
          <circle cx="11" cy="15" r="0.9" fill="var(--kraft)"/>
        </svg>
      </div>
      <div class="contact-rule"></div>
      <div class="contact-details">
        <p class="service-area">Sydney wide removals +<br>relocation services</p>
        <p class="contact-email">rtbremovals@quillpost.example</p>
        <p class="contact-phone">0417 282 934</p>
      </div>
    </div>
  </section>
</body>
</html>
```